Kindlebrook Leaflet

We need a 4 page flyer designed to show off the 3 different programmes that we can offer to schools. They all have different brand guidelines and different companies and it's a leaflet to incorporate all of the brands. The leaflet needs to be clear, concise and eye catching. The final design should encourage any reader to find out more about what we do and understand that one of our programmes could help to inspire young people. I have attached a rough draft of content/ideas but it needs much more of a design flair (in particular the front cover). We work with Olympians/Paralympians so it would be great to get that message across and also the idea of happy and active children.<br/><br/>Websites for the programmes are:<br/>Bright Steps Learning: www.brightstepslearning.org<br/>Fenwix: www.fenwixa.co.uk<br/>Heroes of Tomorrow: www.heroesoftomorrow.com<br/><br/>I have also uploaded some images/logos etc.<br/><br/>Font for Fenwixa = Oxygen<br/><br/>Brand Guidelines attached for HoT

```html
<!DOCTYPE html>
<html lang="en">
<head>
<meta charset="utf-8">
<title>Kindlebrook Leaflet – Spreads</title>
<link href="https://fonts.googleapis.com/css2?family=Archivo:wght@400;700;800&family=Arimo:wght@400&family=Libre+Baskerville:ital@1&display=swap" rel="stylesheet">
<style>
  :root {
    --purple: #8d2b8c;
    --yellow: #f6c700;
    --red: #d7202f;
    --lime: #b6d335;
    --blue: #1e98d7;
    --ink: #1c1c1c;
    --navy: #1f2a44;
    --paper: #ffffff;
    --backdrop: #eeeeee;
  }
  * { margin: 0; padding: 0; box-sizing: border-box; }
  html, body { width: 1200px; height: 1000px; overflow: hidden; }
  body { background: var(--backdrop); font-family: "Archivo", Arial, sans-serif; color: var(--ink); position: relative; }

  .spread { position: absolute; left: 270px; width: 660px; height: 466px; background: var(--paper); box-shadow: 0 4px 12px rgba(0,0,0,.18); overflow: hidden; }
  .spread--outer { top: 22px; }
  .spread--inner { top: 510px; }
  .spread::after { content: ""; position: absolute; left: 329px; top: 0; width: 2px; height: 100%; background: linear-gradient(90deg, rgba(0,0,0,.08), rgba(0,0,0,0)); }

  .photo { position: absolute; }
  .photo--classroom { background: linear-gradient(160deg, #6d6660, #a08478 60%, #b3332f); }
  .photo--coach { background: linear-gradient(120deg, #c9483c 0%, #d8a96a 45%, #e0b27a 100%); }
  .photo--plank { background: linear-gradient(135deg, #4f9c6f 0%, #caa07e 45%, #d65245 75%, #c9b7a0 100%); }
  .photo--group { background: linear-gradient(150deg, #9a9489 0%, #6a6560 45%, #c2a58b 100%); }
  .photo--assembly { background: linear-gradient(170deg, #3a6ea8, #a99f95 60%, #7d8a9b); }
  .photo--drawing { background: linear-gradient(140deg, #e9e4dc, #c8483c 55%, #d9a46c); }
  .photo--dance { background: linear-gradient(180deg, #d9d4cc 0%, #b9b2a6 45%, #d29a5c 70%, #c78a4c 100%); }

  .tile { position: absolute; }
  .tile--purple { background: var(--purple); }
  .tile--yellow { background: var(--yellow); }
  .tile--red { background: var(--red); }
  .tile--lime { background: var(--lime); }
  .tile--blue { background: var(--blue); }

  .grid-line { position: absolute; background: #fff; }

  .statement { position: absolute; display: flex; align-items: center; justify-content: center; text-align: center; color: #fff; font-weight: 700; text-transform: uppercase; }
  .statement--values { left: 165px; top: 105px; width: 165px; height: 125px; background: var(--red); font-size: 17px; line-height: 22px; }
  .statement--hub { left: 330px; top: 105px; width: 160px; height: 125px; background: var(--purple); font-size: 16px; line-height: 21px; }
  .statement--best { left: 165px; top: 320px; width: 165px; height: 146px; background: var(--yellow); font-size: 17px; line-height: 22px; }

  .body-copy { position: absolute; width: 148px; font-family: "Arimo", Arial, sans-serif; font-size: 8.4px; line-height: 11.1px; color: #222; white-space: nowrap; }

  .brand { position: absolute; display: flex; align-items: center; gap: 5px; font-weight: 700; white-space: nowrap; }
  .brand__dot { display: inline-block; border-radius: 50%; }
  .brand__square { display: inline-block; }
  .brand--steps { left: 14px; top: 36px; font-size: 11px; color: var(--red); }
  .brand--steps .brand__dot { width: 12px; height: 12px; background: var(--red); }
  .brand--fenwixa { left: 512px; top: 28px; font-size: 26px; color: var(--purple); }
  .brand--fenwixa .brand__dot { width: 14px; height: 14px; background: var(--purple); }
  .brand--heroes { left: 14px; top: 262px; font-size: 11.5px; color: var(--navy); }
  .brand--heroes .brand__square { width: 16px; height: 16px; background: var(--navy); }

  .cover-title { position: absolute; left: 498px; top: 18px; width: 160px; font-weight: 800; font-size: 21px; line-height: 23px; text-transform: uppercase; color: var(--ink); }
  .cover-title em { font-family: "Libre Baskerville", Georgia, serif; font-style: italic; font-weight: 400; text-transform: none; font-size: 20px; }

  .cover-bottom { position: absolute; left: 330px; top: 360px; width: 248px; height: 106px; }
  .programmes-title { position: absolute; left: 18px; top: 16px; font-weight: 800; font-size: 21px; line-height: 22px; text-transform: uppercase; color: var(--ink); white-space: nowrap; }
  .partner-row { position: absolute; left: 20px; top: 76px; display: flex; gap: 8px; align-items: center; font-size: 7.5px; font-weight: 700; }
  .partner-row .brand { position: static; }
  .brand--heroes-mini { color: var(--navy); }
  .brand--fenwixa-mini { color: var(--purple); font-size: 10px; }
  .brand--steps-mini { color: var(--red); }
</style>
</head>
<body>

<section class="spread spread--outer">
  <div class="brand brand--steps"><span class="brand__dot"></span>Bright Steps Learning</div>
  <div class="photo photo--classroom" style="left:165px;top:0;width:165px;height:105px" role="img" aria-label="Pupils seated on a classroom floor watching an athlete presentation"></div>
  <p class="body-copy" style="left:14px;top:68px">Lorem ipsum dolor sit amet, consec<br>tetur adipiscing elit. Nullam tellus<br>neque, pretium quis felis eget, ves<br>tibulum hendrerit magna. Sed sed<br>volutpat dui. Aenean posuere biben<br>dum lacinia. Fusce ac dui vitae<br>neque porttitor hendrerit ac eget<br>quam. Donec placerat pellentesque<br>risus et interdum. Nunc at ex at dui<br>consectetur ornare a efficitur nibh.<br>Aliquam id ex dignissim, sodales<br>magna in, fringilla metus. Nunc ut<br>nunc in ligula ornare congue congue<br>nec erat.</p>
  <div class="statement statement--values">Activate<br>Educate<br>Motivate<br>Innovate</div>
  <div class="photo photo--coach" style="left:0;top:230px;width:330px;height:236px" role="img" aria-label="Athlete coach kneeling beside a young boy doing an exercise on a gym mat"></div>

  <div class="tile tile--purple" style="left:330px;top:0;width:82px;height:112px"></div>
  <div class="tile tile--yellow" style="left:412px;top:0;width:82px;height:112px"></div>
  <h1 class="cover-title">Fitter kids<br>do <em>Better</em><br>at school</h1>
  <div class="photo photo--plank" style="left:330px;top:112px;width:330px;height:248px" role="img" aria-label="Smiling children holding a plank position on a school hall floor"></div>
  <div class="tile tile--red" style="left:330px;top:112px;width:82px;height:83px"></div>
  <div class="tile tile--lime" style="left:578px;top:278px;width:82px;height:82px"></div>
  <div class="tile tile--blue" style="left:578px;top:360px;width:82px;height:106px"></div>
  <div class="grid-line" style="left:412px;top:112px;width:1px;height:248px"></div>
  <div class="grid-line" style="left:494px;top:112px;width:1px;height:248px"></div>
  <div class="grid-line" style="left:578px;top:112px;width:1px;height:248px"></div>
  <div class="grid-line" style="left:330px;top:195px;width:330px;height:1px"></div>
  <div class="grid-line" style="left:330px;top:278px;width:330px;height:1px"></div>
  <div class="cover-bottom">
    <h2 class="programmes-title">Role-model led<br>programmes</h2>
    <div class="partner-row">
      <span class="brand brand--heroes-mini">Heroes of Tomorrow</span>
      <span class="brand brand--fenwixa-mini">Fenwixa</span>
      <span class="brand brand--steps-mini">Bright Steps Learning</span>
    </div>
  </div>
</section>

<section class="spread spread--inner">
  <div class="photo photo--group" style="left:0;top:0;width:330px;height:235px" role="img" aria-label="Group of boys with arms around each other in a sports hall"></div>
  <div class="brand brand--heroes"><span class="brand__square"></span>Heroes of Tomorrow</div>
  <p class="body-copy" style="left:14px;top:298px">Lorem ipsum dolor sit amet, consec<br>tetur adipiscing elit. Nullam tellus<br>neque, pretium quis felis eget, ves<br>tibulum hendrerit magna. Sed sed<br>volutpat dui. Aenean posuere biben<br>dum lacinia. Fusce ac dui vitae<br>neque porttitor hendrerit ac eget<br>quam. Donec placerat pellentesque<br>risus et interdum. Nunc at ex at dui<br>consectetur ornare a efficitur nibh.<br>Aliquam id ex dignissim, sodales<br>magna in, fringilla metus. Nunc ut<br>nunc in ligula ornare congue congue<br>nec erat.</p>
  <div class="photo photo--drawing" style="left:165px;top:235px;width:165px;height:85px" role="img" aria-label="Child writing on a sheet of paper on the floor"></div>
  <div class="statement statement--best">Be your<br>personal<br>best with us</div>

  <div class="photo photo--assembly" style="left:330px;top:0;width:160px;height:105px" role="img" aria-label="Pupils in a school hall facing a projected screen"></div>
  <div class="statement statement--hub">The hub<br>for clubs</div>
  <div class="brand brand--fenwixa"><span class="brand__dot"></span>Fenwixa</div>
  <p class="body-copy" style="left:506px;top:72px">Lorem ipsum dolor sit amet, consec<br>tetur adipiscing elit. Nullam tellus<br>neque, pretium quis felis eget, ves<br>tibulum hendrerit magna. Sed sed<br>volutpat dui. Aenean posuere biben<br>dum lacinia. Fusce ac dui vitae<br>neque porttitor hendrerit ac eget<br>quam. Donec placerat pellentesque<br>risus et interdum. Nunc at ex at dui<br>consectetur ornare a efficitur nibh.<br>Aliquam id ex dignissim, sodales<br>magna in, fringilla metus. Nunc ut<br>nunc in ligula ornare congue congue<br>nec erat.</p>
  <div class="photo photo--dance" style="left:330px;top:232px;width:330px;height:234px" role="img" aria-label="Young girls posing together on a wooden sports hall floor"></div>
</section>

</body>
</html>
```